Enterteinment new company in Costa Rica who wants to attract international artists

We need a business design for s new company from Costa Rica Called The Copper Lanterns. Our core business is Produce Alternative Rock Concerts. We would like to see a very creative business card connected to music ideas. Our logo is Black so we would like to see not too many colors on it. Silver letters would be great combined with black.

Target Market(s)

Entertainment

Industry/Entity Type

Entertainment

Contact Information for Business Card

We would like something different, creative.

Font styles to use
Other font styles liked:
• voltaire

Colors
000000
ffffff

Requirements
Must have
• We are looking for a creative business card
Nice to have
• liked to music

```html
<!DOCTYPE html>
<html lang="en">
<head>
<meta charset="utf-8">
<title>The Copper Lanterns – Business Card</title>
<link rel="stylesheet" href="https://fonts.googleapis.com/css2?family=Source+Sans+3:wght@400;600&display=swap">
<style>
  :root {
    --backdrop: #5a4f4a;
    --card-black: #141414;
    --card-edge: #0b0b0b;
    --silver: #b9b9b9;
    --white: #f4f4f4;
    --muted: #d6d6d6;
    --rule: #4a4a4a;
    --stave: #2c2c2c;
  }
  * { box-sizing: border-box; margin: 0; padding: 0; }
  html, body { width: 1200px; height: 771px; overflow: hidden; }
  body {
    background: var(--backdrop);
    font-family: "Source Sans 3", sans-serif;
    position: relative;
  }
  .card {
    position: absolute;
    top: 231px;
    width: 540px;
    height: 309px;
    background: var(--card-black);
    border: 1px solid var(--card-edge);
    box-shadow: 0 10px 24px rgba(0,0,0,0.35);
    overflow: hidden;
  }
  .card-front { left: 40px; }
  .card-back { left: 620px; }

  /* five-line music stave running along the lower edge */
  .stave {
    position: absolute;
    left: 0; right: 0; bottom: 22px;
    height: 33px;
    background: repeating-linear-gradient(
      to bottom,
      var(--stave) 0 1px,
      transparent 1px 8px
    );
  }
  .card-front .stave { bottom: 24px; }

  .brand {
    display: flex;
    flex-direction: column;
    align-items: center;
    gap: 14px;
  }
  .brand-dot {
    width: 62px; height: 62px;
    border-radius: 50%;
    background: currentColor;
  }
  .brand-name {
    font-weight: 600;
    line-height: 1.05;
    text-align: center;
  }
  .card-front .brand {
    position: absolute; inset: 0 0 40px 0;
    justify-content: center;
    color: var(--silver);
  }
  .card-front .brand-name { font-size: 40px; }

  .card-back .brand {
    position: absolute;
    left: 28px; top: 66px;
    width: 250px;
    color: var(--white);
  }
  .card-back .brand-dot { width: 54px; height: 54px; }
  .card-back .brand-name { font-size: 31px; }

  .divider {
    position: absolute;
    left: 292px; top: 66px;
    width: 1px; height: 170px;
    background: var(--rule);
  }
  .contact {
    position: absolute;
    left: 308px; top: 40px;
    color: var(--muted);
  }
  .person-name {
    font-size: 24px;
    font-weight: 600;
    color: var(--white);
    line-height: 1.1;
  }
  .person-role { font-size: 13px; margin-bottom: 10px; }
  .address { font-size: 13px; line-height: 1.3; margin-bottom: 8px; }
  .contact-list { list-style: none; font-size: 13px; line-height: 1.55; }
  .contact-list li { display: flex; align-items: center; gap: 7px; }
  .contact-list svg { width: 11px; height: 11px; fill: var(--muted); flex: none; }
</style>
</head>
<body>

<section class="card card-front">
  <div class="stave" aria-hidden="true"></div>
  <div class="brand">
    <span class="brand-dot"></span>
    <span class="brand-name">The Copper Lanterns</span>
  </div>
</section>

<section class="card card-back">
  <div class="stave" aria-hidden="true"></div>
  <div class="brand">
    <span class="brand-dot"></span>
    <span class="brand-name">The Copper Lanterns</span>
  </div>

  <div class="divider"></div>

  <div class="contact">
    <p class="person-name">Daniel Marsh</p>
    <p class="person-role">Managing Member</p>
    <p class="address">Avenida Central 218,<br>San José, Costa Rica</p>
    <ul class="contact-list">
      <li>
        <svg viewBox="0 0 12 12" aria-hidden="true"><path d="M2.5 0.8l2 2.4-1.1 1.3c.7 1.5 1.9 2.7 3.4 3.4l1.3-1.1 2.4 2-1.2 2.2C5.4 10.6 1.4 6.6 0.4 2z"/></svg>
        +506 2208 3371
      </li>
      <li>
        <svg viewBox="0 0 12 12" aria-hidden="true"><path d="M3 0h5v3H3zM1 4h10v6H9v2H3v-2H1zM4 8v3h4V8z"/></svg>
        +506 2208 3372
      </li>
      <li>
        <svg viewBox="0 0 12 12" aria-hidden="true"><path d="M3 0h6v12H3zM4 1.5v8h4v-8z"/></svg>
        +506 8554 1980
      </li>
      <li>
        <svg viewBox="0 0 12 12" aria-hidden="true"><path d="M0 2h12v1L6 7 0 3zM0 4.3l6 4 6-4V10H0z"/></svg>
        daniel@lanternsite.com
      </li>
      <li>
        <svg viewBox="0 0 12 12" aria-hidden="true"><path d="M6 0a6 6 0 1 0 0 12A6 6 0 0 0 6 0zm0 1.2c.8.8 1.3 2.5 1.4 4.2H4.6C4.7 3.7 5.2 2 6 1.2zM1.3 6.6h2.2c.1 1.5.4 2.8 1 3.8a4.8 4.8 0 0 1-3.2-3.8zm0-1.2a4.8 4.8 0 0 1 3.2-3.8c-.6 1-.9 2.3-1 3.8zm3.3 1.2h2.8C7.3 8.3 6.8 10 6 10.8 5.2 10 4.7 8.3 4.6 6.6zm3.9 0h2.2a4.8 4.8 0 0 1-3.2 3.8c.6-1 .9-2.3 1-3.8zm0-1.2c-.1-1.5-.4-2.8-1-3.8a4.8 4.8 0 0 1 3.2 3.8z"/></svg>
        www.lanternsite.com
      </li>
    </ul>
  </div>
</section>

</body>
</html>
```